Cocktail Menu for my Breakfast Cafe

I would like a simple drink menu designed. I have uploaded the info of names and prices as well as our restaurant logo - We are an old meets new kind of theme - lots of antiques in our restaurant with buffalo heads - wood everywhere. I would just like something simple and rustic looking with a modern twist - the colors that I would like are neutral tones - browns/woods / Taupes etc

Target Market(s)

Variety - families and trendy hipsters on the weekend and Business People during the week

Industry/Entity Type

Cafe

Font styles to use
Serif

Colors

Designer to choose colors to be used in the design.

Requirements
Must have
• must fit on 127 X 178 paper - it will be a table tent menu so there will need to be a front and back design - The front should have the entire drink menu and the back can just be a solid color or maybe something with our logo
Nice to have
• Traditional with a modern twist
• Saloon style
• wood motif perhaps?
Should not have
• I'm pretty flexible with ideas

```html
<!DOCTYPE html>
<html lang="en">
<head>
<meta charset="utf-8">
<title>Ironhorn Cafe – Boozy Breakfast Table Tent</title>
<link rel="stylesheet" href="https://fonts.googleapis.com/css2?family=Playfair+Display+SC:wght@700;900&family=IM+Fell+English+SC&family=Old+Standard+TT:wght@400;700&display=swap">
<style>
  :root{
    --backdrop:#1c2327;
    --paper:#d9cbb0;
    --paper-light:#e3d7bf;
    --paper-dark:#c8b797;
    --ink:#2a221b;
    --ink-soft:#4d4236;
    --rule:#3a3027;
    --sketch-dark:#5b5148;
    --sketch-light:#b9ab92;
  }
  *{box-sizing:border-box;margin:0;padding:0}
  html,body{width:1112px;height:1200px;overflow:hidden}
  body{
    background:var(--backdrop);
    font-family:"Old Standard TT",Georgia,serif;
    color:var(--ink);
    display:flex;align-items:center;justify-content:center;gap:40px;
  }
  .panel{
    width:480px;height:672px;
    background:radial-gradient(ellipse at 30% 20%,var(--paper-light),var(--paper) 55%,var(--paper-dark));
    position:relative;
    overflow:hidden;
  }
  /* Back panel */
  .back{padding:70px 56px 40px;display:flex;flex-direction:column;align-items:center}
  .brand{
    font-family:"Playfair Display SC",Georgia,serif;font-weight:900;
    font-size:60px;line-height:1;color:var(--ink);text-align:center;letter-spacing:1px;
    display:flex;align-items:center;gap:14px;
  }
  .brand-dot{width:22px;height:22px;border-radius:50%;background:var(--ink)}
  .brand-rule{width:300px;height:2px;background:var(--rule);margin:22px 0 36px}
  .story{font-size:15px;line-height:1.7;text-align:center;color:var(--ink-soft);letter-spacing:.5px;text-transform:uppercase}
  .web{margin-top:auto;font-size:13px;letter-spacing:3px;text-transform:uppercase;color:var(--ink-soft)}
  /* Front panel */
  .front{display:flex}
  .sketch{
    width:190px;height:100%;
    background:linear-gradient(100deg,var(--sketch-dark) 0%,var(--sketch-light) 75%,transparent 100%);
    opacity:.55;
  }
  .menu{flex:1;padding:44px 30px 30px 14px}
  .menu-title{
    font-family:"Playfair Display SC",Georgia,serif;font-weight:900;
    font-size:46px;line-height:.9;
  }
  .menu-title small{display:block;font-size:27px;font-weight:700;letter-spacing:1px}
  .drinks{list-style:none;margin-top:26px;display:flex;flex-direction:column;gap:26px}
  .tag{
    display:flex;align-items:center;gap:8px;
    border:1.5px solid var(--rule);padding:5px 10px 5px 8px;
    font-family:"IM Fell English SC",Georgia,serif;font-size:21px;line-height:1.05;
  }
  .tag::before{content:"";flex:none;width:9px;height:9px;border-radius:50%;border:1.5px solid var(--rule)}
  .details{display:flex;justify-content:space-between;margin:6px 4px 0 18px;font-size:11px;text-transform:uppercase;letter-spacing:.6px;color:var(--ink-soft)}
  .details .mix{max-width:130px;line-height:1.35}
  .price{font-size:13px;font-weight:700;color:var(--ink);white-space:nowrap}
</style>
</head>
<body>
  <section class="panel back">
    <h1 class="brand"><span class="brand-dot"></span>Ironhorn<br>Cafe</h1>
    <div class="brand-rule"></div>
    <p class="story">Our cafe sits in a heritage building that has watched the town grow since the early days. Come for the coffee, stay for the stories, and enjoy a hearty breakfast among the antiques, the timber and the buffalo heads.</p>
    <p class="web">ironhorncafe.ca</p>
  </section>

  <section class="panel front">
    <div class="sketch" role="img" aria-label="Pencil sketch of a shaggy long-horned bull in profile"></div>
    <div class="menu">
      <h2 class="menu-title">Boozy<small>Breakfast</small></h2>
      <ul class="drinks">
        <li><div class="tag">Simple Ceasar</div>
          <div class="details"><span class="mix">Vodka, tomato clam juice, Worcestershire, pickled bean</span><span class="price">7.00 · Double shot 11.00</span></div></li>
        <li><div class="tag">Someone Spiked My Juice!</div>
          <div class="details"><span class="mix">Vodka, orange juice</span><span class="price">6.00 · Double shot 10.00</span></div></li>
        <li><div class="tag">Maddox's N Coffee</div>
          <div class="details"><span class="mix">Cream liqueur, coffee</span><span class="price">6.00</span></div></li>
        <li><div class="tag">Madame Mimosa!</div>
          <div class="details"><span class="mix">Prosecco, orange juice, strawberries</span><span class="price">7.00</span></div></li>
        <li><div class="tag">Local Brew</div>
          <div class="details"><span class="mix">Prairie Blonde, Ridge Pale Ale</span><span class="price">6.00</span></div></li>
      </ul>
    </div>
  </section>
</body>
</html>
```